Suchen ansprechendes & seriöses Urkunden/Zertifikat Design für Webseite & Druck
Zielgruppe
Auf unserer Webseite http://rege-im-alter-netz.de können sich Unternehmen, Institutionen und Vereine ihre Seniorenfreundlichkeit durch ein Zertifikat bestätigen und zertifizieren lassen.
Unsere Kundengruppen: Hotel – Gastronomie – Wellness – Reisen und Touristik – Touristikregionen – Seniorenshop – Onlineshop – Unternehmen als Dienstleister – Medizin und Health-Service – Apotheke – Altenheim – Pflegeheim – Seniorenheim – Vereine – Seniorenservice – Zahnärzte – Fitnessstudio – Sportstudio – Physiotherapie – Sportverein – Golfclub – und viele weitere seniorenfreundliche Institutionen.
Aufgabenstellung
Auftrag- Ausschreibung:
- Erstellung eines Design:
- Urkunde für Webseite rege-im-alter-netz.de - Das Zertifikat "Rege im Alter“
Funktion:
Kunde erkennt das Zertifikat - Logo auf einer Webseite und Klickt auf dieses.
Er wird weitergeleitet auf eine Unterseite, worin die Richtlinien und die Urkunde sichtbar wird.
Zielgruppe:
- Unternehmen, welche das Zertifikat auf Ihre Webseite setzen. Die Urkunde gibt Auskunft, dass der Dienstleister einen besonderen Service für Senioren ausübt. Die Urkunde ist sichtbar auf der Webseite, indem das Logo angeklickt wird. Die Urkunde gibt es ebenfalls als Download, damit der Kunde diese in seinen Geschäftsräumen aufhängen kann oder diese in seinen Werbeunterlagen präsentieren kann.
- Verbraucher sollen beeindruckt sein, von der Urkunde, welches Vertrauen ausstrahlt, aber auch Seriosität
Folgende Ausstrahlung soll die Urkunde haben:
- Soll Mitbewerber des Zertifikatsinhaber beeindrucken und das Verlangen aufzeigen, sich ebenfalls zertifizieren zu lassen ( ca: 70% der Kunden sind Mitbewerber … ). Nach dem Motto "Das Logo ist super und edel, das muss ich auch haben!"
- Der Kunde als Verbraucher soll Vertrauen gewinnen, die Daten sollen gut sichtbar sein, aber nicht verkitscht wie eine Urkunde bei einer Kaffeefahrt. Der Verbraucher geht auf das Zertifikat und kommt zur Urkunde, deshalb soll die Farbe, und Darstellung, Seriosität des Unternehmens ausstrahlen.
Sonstiges
- Die Urkunde soll dem neuen Design unserer Seite (zu sehen unter: http://guetesiegel-welt.de) angepasst sein.
- Vor Auftragsendvergabe erhalten Sie noch ein telefonisches Briefing über unsere Erfahrungswerte
Link zur bestehenden alten Webseite (Altes Design): http://rege-im-alter-netz.de
Info Verbraucher: http://www.rege-im-alter-netz.de/verbraucher/
Info zum Zertifikat: http://www.rege-im-alter-ne..

```html
<!DOCTYPE html>
<html lang="de">
<head>
<meta charset="utf-8">
<title>Zertifikat – Rege im Alter</title>
<link href="https://fonts.googleapis.com/css2?family=Bebas+Neue&family=Raleway:wght@300;400;600;700&display=swap" rel="stylesheet">
<style>
  :root {
    --ink: #1d1d1f;
    --brand-purple: #33268a;
    --frame-blue: #3b3796;
    --frame-grey: #e2dfdb;
    --accent-red: #c8323a;
    --accent-gold: #c9a24a;
    --paper: #ffffff;
    --wash: #f4f1ee;
    --seal: #d9d6d2;
    --seal-ring: #b7b2ac;
  }
  * { margin: 0; padding: 0; box-sizing: border-box; }
  html, body { width: 850px; height: 1200px; overflow: hidden; background: var(--paper); }
  .certificate {
    position: relative; width: 850px; height: 1200px;
    background: var(--paper); color: var(--ink);
    font-family: "Raleway", Arial, sans-serif;
  }
  .background-wash {
    position: absolute; left: 66px; top: 48px; width: 719px; height: 1074px;
    background: radial-gradient(ellipse at 50% 45%, var(--wash) 0%, var(--paper) 75%);
  }
  .frame-art { position: absolute; inset: 0; }
  .title {
    position: absolute; left: 0; right: 0; top: 82px; text-align: center;
    font-family: "Bebas Neue", Impact, sans-serif; font-size: 190px;
    line-height: 1; color: var(--brand-purple); letter-spacing: 2px;
  }
  .subtitle {
    position: absolute; left: 0; right: 0; top: 228px; text-align: center;
    font-weight: 300; font-size: 56px; letter-spacing: 1px; color: var(--ink);
  }
  .details { position: absolute; left: 0; top: 325px; width: 850px; }
  .row { position: absolute; left: 0; display: flex; width: 850px; font-size: 24px; line-height: 30px; }
  .row dt { width: 348px; text-align: right; font-weight: 600; }
  .row dd { margin-left: 12px; font-weight: 400; }
  .confirmed {
    position: absolute; left: 188px; top: 916px; font-size: 24px; font-weight: 600;
  }
  .signature {
    position: absolute; top: 968px; height: 62px; border-radius: 4px;
    background: linear-gradient(90deg, #e9e9e9, #d4d4d4);
  }
  .signature.one { left: 150px; width: 140px; }
  .signature.two { left: 290px; width: 160px; }
  .signer { position: absolute; top: 1032px; font-size: 17px; }
  .signer.one { left: 162px; }
  .signer.two { left: 310px; }
  .seal {
    position: absolute; left: 486px; top: 876px; width: 212px; height: 212px;
    border-radius: 50%; background: var(--seal); border: 8px solid var(--seal-ring);
  }
  .page-number { position: absolute; left: 10px; top: 1172px; font-size: 21px; font-weight: 700; }
</style>
</head>
<body>
<main class="certificate">
  <div class="background-wash"></div>

  <svg class="frame-art" width="850" height="1200" viewBox="0 0 850 1200" aria-hidden="true">
    <rect x="64" y="46" width="722" height="1078" fill="none" stroke="var(--frame-grey)" stroke-width="2"/>
    <!-- top rule -->
    <line x1="285" y1="68" x2="565" y2="68" stroke="var(--frame-blue)" stroke-width="2"/>
    <rect x="419" y="62" width="12" height="12" transform="rotate(45 425 68)" fill="var(--frame-blue)"/>
    <!-- bottom rule -->
    <line x1="285" y1="1117" x2="565" y2="1117" stroke="var(--frame-blue)" stroke-width="2"/>
    <rect x="419" y="1111" width="12" height="12" transform="rotate(45 425 1117)" fill="var(--frame-blue)"/>
    <!-- side rules -->
    <line x1="72" y1="340" x2="72" y2="870" stroke="var(--frame-blue)" stroke-width="2"/>
    <line x1="778" y1="340" x2="778" y2="870" stroke="var(--frame-blue)" stroke-width="2"/>
    <!-- corner accents -->
    <g stroke-width="3" fill="none">
      <path d="M70 140 V56 H160" stroke="var(--accent-red)"/>
      <path d="M78 140 V64 H160" stroke="var(--accent-gold)"/>
      <path d="M780 140 V56 H690" stroke="var(--accent-red)"/>
      <path d="M772 140 V64 H690" stroke="var(--accent-gold)"/>
      <path d="M70 1030 V1114 H160" stroke="var(--frame-blue)"/>
      <path d="M78 1030 V1106 H160" stroke="var(--accent-gold)"/>
      <path d="M780 1030 V1114 H690" stroke="var(--frame-blue)"/>
      <path d="M772 1030 V1106 H690" stroke="var(--accent-gold)"/>
    </g>
  </svg>

  <h1 class="title">ZERTIFIKAT</h1>
  <p class="subtitle">REGE IM ALTER</p>

  <dl class="details">
    <div class="row" style="top:0"><dt>Zertifikat ID:</dt><dd>7250441e9e</dd></div>
    <div class="row" style="top:66px"><dt>Anbieter:</dt><dd>Rege im Alter<br>Ihr Zertifizierungsdienst</dd></div>
    <div class="row" style="top:144px"><dt>Status:</dt><dd>aktiv</dd></div>
    <div class="row" style="top:200px"><dt>Unternehmen:</dt><dd>Senioren Service Lindner<br>Ahornweg 7<br>54321 Musterort<br>Deutschland<br>info@lindner-service.org</dd></div>
    <div class="row" style="top:370px"><dt>Vertretungs-<br>berechtigter:</dt><dd>Frau Katrin<br>Lindner</dd></div>
    <div class="row" style="top:460px"><dt>Erstprüfung am:</dt><dd>07.04.2017</dd></div>
    <div class="row" style="top:502px"><dt>gültig bis:</dt><dd>07.04.2019</dd></div>
  </dl>

  <p class="confirmed">Bestätigt von:</p>
  <div class="signature one" role="img" aria-label="Handschriftliche Unterschrift H. Berger"></div>
  <div class="signature two" role="img" aria-label="Handschriftliche Unterschrift C. Wallner"></div>
  <span class="signer one">H. Berger</span>
  <span class="signer two">C. Wallner</span>

  <div class="seal" role="img" aria-label="Prüfsiegel"></div>

  <span class="page-number">19</span>
</main>
</body>
</html>
```